Training material templates, Word and PowerPoint

I conduct management training for executive level clients. I am looking to develop a template for the training materials that has a consistent high quality look. These training materials include participant handouts and workbooks, training information sheets and PowerPoint presentations.
I have previously used lumen yard to design a logo, business cards and letterheads, which are attached as examples.

Target Market(s)

Professionals

Requirements
Nice to have
• My preference for body text in Word documents is Calibri 11pt, with headings being a compatible font.
Preference is also for text in Word documents to be single height, with 6 point spacing before and after

```html
<!DOCTYPE html>
<html lang="en">
<head>
<meta charset="utf-8">
<title>Halden Consulting – Document Template Suite</title>
<link href="https://fonts.googleapis.com/css2?family=Open+Sans:ital,wght@0,400;0,600;0,700;1,400&display=swap" rel="stylesheet">
<style>
:root{
  --blue:#1e9ad6;
  --grey:#858585;
  --grey-dark:#6b6b6b;
  --ink:#555555;
  --soft:#8e8e8e;
  --pale:#e4e4e4;
  --canvas:#efefef;
  --white:#ffffff;
}
*{box-sizing:border-box;margin:0;padding:0}
html,body{width:1200px;height:3150px;overflow:hidden}
body{background:var(--canvas);font-family:'Open Sans',sans-serif;color:var(--ink);position:relative}
.page{position:absolute;width:348px;height:489px;background:var(--white);box-shadow:0 3px 9px rgba(0,0,0,.13);overflow:hidden}
.page.inner{border-bottom:4px solid var(--grey)}
.page.dark{background:var(--grey)}
.abs{position:absolute}
.c1{left:39px}.c2{left:414px}.c3{left:790px}
.r1{top:45px}.r2{top:559px}.r3{top:1076px}.r4{top:1592px}.r5{top:2109px}.r6{top:2626px}

/* brand */
.brand{display:flex;align-items:center;gap:6px;font-weight:600;letter-spacing:2px;color:var(--grey-dark)}
.brand .dot{border-radius:50%;background:var(--blue);flex:none}
.brand-lg{font-size:26px}.brand-lg .dot{width:22px;height:22px}
.brand-md{font-size:17px}.brand-md .dot{width:15px;height:15px}
.brand-sm{font-size:8px;letter-spacing:1px;gap:3px}.brand-sm .dot{width:8px;height:8px}
.brand.on-dark{color:var(--white)}
.header-brand{position:absolute;top:14px;right:22px}

/* cover type */
.cover-title{position:absolute;left:0;width:100%;text-align:center;font-weight:600;font-size:24px;line-height:33px;color:var(--grey-dark)}
.cover-sub{position:absolute;left:0;width:100%;text-align:center;font-size:7px;letter-spacing:4.5px;font-weight:600;color:var(--ink)}
.web{position:absolute;left:0;width:100%;text-align:center;font-size:6.5px;letter-spacing:4px;color:var(--ink)}
.rule{position:absolute;height:2px;width:30px;background:var(--blue)}
.socials{position:absolute;display:flex;gap:3px}
.socials span{width:9px;height:9px;border:1px solid currentColor;border-radius:50%}

/* interior */
.heading{position:absolute;left:42px;font-size:11px;font-weight:600;color:var(--ink)}
.copy{position:absolute;left:42px;width:264px;font-size:5px;line-height:7.3px;color:var(--soft);text-align:justify}
.copy p+p{margin-top:7px}
.footer{position:absolute;left:42px;right:42px;bottom:12px;display:flex;justify-content:space-between;font-size:5.5px;color:var(--ink)}

/* toc */
.toc{position:absolute;left:42px;top:92px;width:264px;font-size:5.5px;line-height:12px;color:var(--ink)}
.toc li{list-style:none;display:flex}
.toc li::after{content:"";flex:1;border-bottom:1px dotted #aaa;margin:0 2px 4px;order:1}
.toc li b{font-weight:400;order:2}
.toc .l2{padding-left:6px}.toc .l3{padding-left:18px}.toc .l4{padding-left:14px}

/* agenda */
.agenda{position:absolute;left:0;top:163px;width:100%}
.agenda li{list-style:none;height:37.8px;position:relative;font-size:8px;color:var(--soft)}
.agenda li::before{content:"";position:absolute;left:138px;top:-2px;width:20px;height:20px;border-radius:50%;background:var(--blue)}
.agenda li::after{content:"";position:absolute;left:144px;top:5px;width:5px;height:5px;border-top:1.3px solid #fff;border-right:1.3px solid #fff;transform:rotate(45deg)}
.agenda li span{position:absolute;left:178px;top:3px}

/* tables */
.grid{position:absolute;left:42px;width:266px;border-collapse:collapse;font-size:5.5px;color:var(--soft);text-align:center}
.grid th{color:#fff;font-weight:600;height:13px}
.grid td{height:12.6px;border-bottom:1px solid #ececec}
.grid .b{background:var(--blue)}.grid .g{background:var(--grey)}.grid .d{background:#5f5f5f}

.photo{position:absolute}
.band{position:absolute;left:0;width:100%;background:var(--grey)}
</style>
</head>
<body>

<!-- Row 1 : covers -->
<section class="page c1 r1">
  <div class="abs" style="left:0;top:0;width:100%;height:15px;background:var(--grey);color:#fff;font-size:6.5px;text-align:center;line-height:15px">Month, 2021</div>
  <h1 class="cover-title" style="top:44px">HALDEN CONSULTING<br>TEMPLATE</h1>
  <div class="cover-sub" style="top:118px">SUBTITLE GOES HERE</div>
  <div class="abs" style="left:0;width:100%;top:350px;display:flex;justify-content:center"><div class="brand brand-lg"><span class="dot"></span>HALDEN</div></div>
  <div class="web" style="top:466px">WWW.YOURWEBSITE.COM</div>
</section>

<section class="page c2 r1">
  <div class="rule" style="left:159px;top:40px"></div>
  <h1 class="cover-title" style="top:50px;color:var(--blue)">HALDEN CONSULTING<br>TEMPLATE</h1>
  <div class="cover-sub" style="top:121px;color:var(--blue)">SUBTITLE GOES HERE</div>
  <div class="socials" style="left:151px;top:162px;color:var(--blue)"><span></span><span></span><span></span><span></span></div>
  <div class="abs" style="left:0;width:100%;top:195px;text-align:center;font-size:7.5px;color:var(--blue)">Month, 2021</div>
  <div class="abs" style="left:0;width:100%;top:386px;display:flex;justify-content:center"><div class="brand brand-md" style="font-size:22px"><span class="dot" style="width:19px;height:19px"></span>HALDEN</div></div>
  <div class="web" style="top:466px;color:var(--blue)">WWW.YOURWEBSITE.COM</div>
</section>

<section class="page c3 r1 dark">
  <div class="web" style="top:36px;color:#fff">WWW.YOURWEBSITE.COM</div>
  <div class="rule" style="left:32px;top:92px;background:#fff"></div>
  <h1 class="abs" style="left:30px;top:104px;font-size:29px;line-height:40px;font-weight:600;color:#fff">HALDEN CONSULTING<br>TEMPLATE</h1>
  <div class="abs" style="left:32px;top:190px;font-size:7px;letter-spacing:4.5px;font-weight:600;color:#fff">SUBTITLE GOES HERE</div>
  <div class="abs" style="left:32px;top:219px;font-size:7.5px;color:#fff">Month, 2021</div>
  <div class="abs" style="left:122px;top:440px"><div class="brand brand-md on-dark"><span class="dot" style="background:#fff"></span>HALDEN</div></div>
</section>

<!-- Row 2 -->
<section class="page c1 r2">
  <div class="abs" style="left:0;width:100%;top:30px;display:flex;justify-content:center"><div class="brand brand-md"><span class="dot"></span>HALDEN</div></div>
  <h1 class="cover-title" style="top:74px">HALDEN CONSULTING<br>TEMPLATE</h1>
  <div class="cover-sub" style="top:147px;color:var(--blue)">SUBTITLE GOES HERE</div>
  <div class="web" style="top:468px">WWW.YOURWEBSITE.COM</div>
</section>

<section class="page c2 r2">
  <div class="photo" role="img" aria-label="Upward view of glass skyscrapers against a blue cloudy sky" style="left:0;top:0;width:100%;height:342px;background:linear-gradient(160deg,#cfe2f3 0%,#6f98c2 35%,#2f5f92 60%,#9fb9d4 85%,#e6eef6 100%)">
    <div class="abs" style="left:68px;top:0;width:3px;height:100%;background:#fff"></div>
    <div class="abs" style="left:138px;top:0;width:3px;height:100%;background:#fff"></div>
    <div class="abs" style="left:208px;top:0;width:3px;height:100%;background:#fff"></div>
    <div class="abs" style="left:278px;top:0;width:3px;height:100%;background:#fff"></div>
  </div>
  <div class="abs" style="left:0;top:342px;width:100%;height:147px;background:#dcdcdc"></div>
  <h1 class="cover-title" style="top:369px">HALDEN CONSULTING<br>TEMPLATE</h1>
  <div class="abs" style="left:0;width:100%;top:451px;display:flex;justify-content:center"><div class="brand brand-md"><span class="dot"></span>HALDEN</div></div>
</section>

<section class="page c3 r2">
  <div class="photo" role="img" aria-label="Black and white photo of a tall art deco tower above a city skyline" style="left:0;top:0;width:142px;height:100%;background:linear-gradient(180deg,#e2e2e2 0%,#bdbdbd 30%,#7d7d7d 60%,#4e4e4e 100%)"></div>
  <div class="header-brand"><div class="brand brand-sm"><span class="dot"></span>HALDEN</div></div>
  <div class="rule" style="left:160px;top:85px"></div>
  <h2 class="abs" style="left:160px;top:96px;font-size:17px;font-weight:600;color:var(--ink)">Agenda</h2>
  <ul class="agenda">
    <li><span>Add Content 1 Here</span></li>
    <li><span>Add Content 2 Here</span></li>
    <li><span>Add Content 3 Here</span></li>
    <li><span>Add Content 4 Here</span></li>
    <li><span>Add Content 5 Here</span></li>
    <li><span>Add Content 6 Here</span></li>
    <li><span>Add Content 7 Here</span></li>
    <li><span>Add Content 8 Here</span></li>
  </ul>
  <div class="abs" style="right:44px;bottom:18px;font-size:5.5px;color:var(--ink)">Page | 6</div>
</section>

<!-- Row 3 -->
<section class="page inner c1 r3">
  <div class="header-brand"><div class="brand brand-sm"><span class="dot"></span>HALDEN</div></div>
  <h2 class="heading" style="top:60px">Table of Contents</h2>
  <ul class="toc">
    <li>Introduction<b>8</b></li>
    <li class="l2">Your Title Here<b>9</b></li>
    <li class="l3">Your Tile Here<b>10</b></li>
    <li class="l3" style="padding-left:24px">Your Title Here<b>11</b></li>
    <li>Table &amp; Chart 1<b>12</b></li>
    <li>Text with table<b>13</b></li>
    <li class="l2">Content Title 01<b>13</b></li>
    <li class="l2">Content Title 02<b>13</b></li>
    <li>Infographic 1<b>14</b></li>
    <li class="l2">Content 01<b>14</b></li>
    <li>Infographic 2<b>14</b></li>
    <li>Section Title Here<b>15</b></li>
    <li>Profile Data Section<b>16</b></li>
    <li class="l4">Profile Name 01<b>16</b></li>
    <li class="l4">Profile Name 02<b>16</b></li>
    <li class="l4">Profile Name 03<b>16</b></li>
    <li class="l4">Profile Name 04<b>16</b></li>
    <li>Additional Notes<b>17</b></li>
  </ul>
  <footer class="footer"><span>Halden Consulting | © All Rights Reserved</span><span>Page | 7</span></footer>
</section>

<section class="page inner c2 r3">
  <div class="header-brand"><div class="brand brand-sm"><span class="dot"></span>HALDEN</div></div>
  <h2 class="heading" style="top:56px">Introduction</h2>
  <div class="copy" style="top:86px">
    <p>Use this space to outline the key ideas of the session, the goals set for each participant and the practical tools they will take back to their team. Keep every point short, clear and easy to revisit after the workshop ends, so that leaders can return to the notes when a real decision is on the table and apply what they learned.</p>
    <p>Each module opens with a short overview of the theme, followed by guided questions, worked examples and a space for personal reflection and action planning.</p>
    <p>Write the purpose of the programme here, who it is designed for and how the material should be used during and after each session. Explain how the handouts, the workbook and the slides fit together, and where participants can find support once the course is over and the real work begins back in the office.</p>
  </div>
  <footer class="footer"><span>Halden Consulting | © All Rights Reserved</span><span>Page | 8</span></footer>
</section>

<section class="page inner c3 r3">
  <div class="header-brand"><div class="brand brand-sm"><span class="dot"></span>HALDEN</div></div>
  <h2 class="heading" style="top:56px">Your Title Here</h2>
  <div class="copy" style="top:86px;column-count:2;column-gap:20px;height:336px;overflow:hidden">
    <p>Use this space to outline the key ideas of the session, the goals set for each participant and the practical tools they will take back to their team. Keep every point short, clear and easy to revisit after the workshop ends, so leaders can return to these notes later.</p>
    <p>Each module opens with a short overview of the theme, followed by guided questions, worked examples and a space for personal reflection and planning.</p>
    <p>Write the purpose of the programme here, who it is designed for and how the material should be used during and after each session, with clear links between the slides and the workbook.</p>
    <p>Leaders learn best when ideas are tied to real choices. Add a short case, a checklist or a set of prompts that help the group test each idea against their own team and goals.</p>
    <p>Close each section with three questions to discuss in pairs and one commitment to record before the next session begins, so progress can be reviewed together.</p>
    <p>Use this space to outline the key ideas of the session, the goals set for each participant and the practical tools they will take back to their team. Keep every point short, clear and easy to revisit.</p>
    <p>Each module opens with a short overview of the theme, followed by guided questions, worked examples and a space for personal reflection and planning after the session.</p>
    <p>Leaders learn best when ideas are tied to real choices. Add a short case, a checklist or a set of prompts that help the group test each idea against their own team.</p>
  </div>
  <footer class="footer"><span>Halden Consulting | © All Rights Reserved</span><span>Page | 9</span></footer>
</section>

<!-- Row 4 -->
<section class="page inner c1 r4">
  <div class="header-brand"><div class="brand brand-sm"><span class="dot"></span>HALDEN</div></div>
  <h2 class="heading" style="top:62px">Your Tile here</h2>
  <div class="copy" style="top:88px"><p>Use this space to outline the key ideas of the session, the goals set for each participant and the practical tools they will take back to their team. Keep every point short, clear and easy to revisit after the workshop ends, so leaders can return to these notes when a real decision is on the table and apply what they learned with confidence.</p></div>
  <svg class="abs" style="left:38px;top:155px" width="270" height="140" viewBox="0 0 270 140" aria-hidden="true">
    <g fill="none">
      <ellipse cx="30" cy="20" rx="27" ry="9" fill="#9a9a9a"/><ellipse cx="30" cy="16" rx="27" ry="9" fill="#d6d6d6"/><circle cx="30" cy="14" r="5" fill="#6b6b6b"/>
      <ellipse cx="97" cy="34" rx="27" ry="9" fill="#9a9a9a"/><ellipse cx="97" cy="30" rx="27" ry="9" fill="#d6d6d6"/><circle cx="97" cy="28" r="5" fill="#6b6b6b"/>
      <ellipse cx="165" cy="46" rx="27" ry="9" fill="#9a9a9a"/><ellipse cx="165" cy="42" rx="27" ry="9" fill="#d6d6d6"/><circle cx="165" cy="40" r="5" fill="#6b6b6b"/>
      <ellipse cx="233" cy="32" rx="27" ry="9" fill="#167aab"/><ellipse cx="233" cy="28" rx="27" ry="9" fill="#1e9ad6"/><circle cx="233" cy="26" r="5" fill="#8fd0f0"/>
    </g>
    <g font-family="Open Sans, sans-serif" font-size="7" fill="#1e9ad6" text-anchor="middle">
      <text x="30" y="42">Step 1</text><text x="97" y="56">Step 2</text><text x="165" y="68">Step 3</text><text x="233" y="54">Step 4</text>
    </g>
    <g font-family="Open Sans, sans-serif" font-size="3.6" fill="#999" text-anchor="middle">
      <text x="30" y="50">Write a short note</text><text x="30" y="55">about this step</text><text x="30" y="60">and what it means</text>
      <text x="97" y="64">Write a short note</text><text x="97" y="69">about this step</text><text x="97" y="74">and what it means</text>
      <text x="165" y="76">Write a short note</text><text x="165" y="81">about this step</text><text x="165" y="86">and what it means</text>
      <text x="233" y="62">Write a short note</text><text x="233" y="67">about this step</text><text x="233" y="72">and what it means</text>
    </g>
  </svg>
  <div class="copy" style="top:305px"><p>Add a summary of the process here and how each step builds on the last. Point out which habits matter most and how the group will measure progress over the coming weeks.</p></div>
  <svg class="abs" style="left:42px;top:358px" width="264" height="80" viewBox="0 0 264 80" aria-hidden="true">
    <g fill="none" stroke-width="6">
      <circle cx="46" cy="28" r="22" stroke="#e6e6e6"/><circle cx="46" cy="28" r="22" stroke="#1e9ad6" stroke-dasharray="94 138" transform="rotate(-90 46 28)"/>
      <circle cx="135" cy="28" r="22" stroke="#e6e6e6"/><circle cx="135" cy="28" r="22" stroke="#7a7a7a" stroke-dasharray="48.4 138" transform="rotate(-90 135 28)"/>
      <circle cx="221" cy="28" r="22" stroke="#e6e6e6"/><circle cx="221" cy="28" r="22" stroke="#7a7a7a" stroke-dasharray="76 138" transform="rotate(-90 221 28)"/>
    </g>
    <g font-family="Open Sans, sans-serif" font-size="10" font-weight="600" fill="#555" text-anchor="middle">
      <text x="46" y="32">68%</text><text x="135" y="32">35%</text><text x="221" y="32">55%</text>
    </g>
    <g font-family="Open Sans, sans-serif" font-size="3.6" fill="#999" text-anchor="middle">
      <text x="46" y="62">A short label for this</text><text x="46" y="67">result in the group</text>
      <text x="135" y="62">A short label for this</text><text x="135" y="67">result in the group</text>
      <text x="221" y="62">A short label for this</text><text x="221" y="67">result in the group</text>
    </g>
  </svg>
  <footer class="footer"><span>Halden Consulting | © All Rights Reserved</span><span>Page | 10</span></footer>
</section>

<section class="page inner c2 r4">
  <div class="header-brand"><div class="brand brand-sm"><span class="dot"></span>HALDEN</div></div>
  <h2 class="heading" style="top:56px">Your Title Here</h2>
  <svg class="abs" style="left:42px;top:82px" width="266" height="82" viewBox="0 0 266 82" aria-hidden="true">
    <g font-family="Open Sans, sans-serif" font-size="3.6" fill="#777">
      <text x="0" y="6">100%</text><text x="2" y="21">75%</text><text x="2" y="36">50%</text><text x="2" y="51">25%</text><text x="4" y="66">0%</text>
    </g>
    <g>
      <rect x="32" y="4" width="12" height="62" fill="#e4e4e4"/><rect x="32" y="52" width="12" height="14" fill="#1e9ad6"/>
      <rect x="55" y="4" width="12" height="62" fill="#e4e4e4"/><rect x="55" y="34" width="12" height="32" fill="#7a7a7a"/>
      <rect x="78" y="4" width="12" height="62" fill="#e4e4e4"/><rect x="78" y="30" width="12" height="36" fill="#1e9ad6"/>
      <rect x="101" y="4" width="12" height="62" fill="#e4e4e4"/><rect x="101" y="38" width="12" height="28" fill="#7a7a7a"/>
      <rect x="124" y="4" width="12" height="62" fill="#e4e4e4"/><rect x="124" y="28" width="12" height="38" fill="#1e9ad6"/>
      <rect x="147" y="4" width="12" height="62" fill="#e4e4e4"/><rect x="147" y="22" width="12" height="44" fill="#7a7a7a"/>
      <rect x="170" y="4" width="12" height="62" fill="#e4e4e4"/><rect x="170" y="28" width="12" height="38" fill="#1e9ad6"/>
      <rect x="193" y="4" width="12" height="62" fill="#e4e4e4"/><rect x="193" y="16" width="12" height="50" fill="#7a7a7a"/>
      <rect x="216" y="4" width="12" height="62" fill="#e4e4e4"/><rect x="216" y="6" width="12" height="60" fill="#7a7a7a"/>
      <rect x="239" y="4" width="12" height="62" fill="#e4e4e4"/><rect x="239" y="14" width="12" height="52" fill="#1e9ad6"/>
    </g>
    <g font-family="Open Sans, sans-serif" font-size="3.6" fill="#777" text-anchor="middle">
      <text x="38" y="74">2011</text><text x="61" y="74">2012</text><text x="84" y="74">2013</text><text x="107" y="74">2014</text><text x="130" y="74">2015</text><text x="153" y="74">2016</text><text x="176" y="74">2017</text><text x="199" y="74">2018</text><text x="222" y="74">2019</text><text x="245" y="74">2020</text>
    </g>
  </svg>
  <div class="copy" style="top:180px"><p>Use this space to outline the key ideas of the session, the goals set for each participant and the practical tools they will take back to their team. Keep every point short, clear and easy to revisit after the workshop ends, so leaders can return to these notes when a real decision is on the table and apply what they learned with confidence.</p></div>
  <div class="photo" role="img" aria-label="Black and white photo of hands signing a document" style="left:42px;top:250px;width:264px;height:96px;border-radius:8px;background:linear-gradient(135deg,#5a5a5a 0%,#a5a5a5 45%,#e0e0e0 75%,#8b8b8b 100%)"></div>
  <svg class="abs" style="left:42px;top:326px" width="264" height="40" viewBox="0 0 264 40" aria-hidden="true">
    <g stroke="#fff" stroke-width="2">
      <polygon points="46,2 63,11 63,29 46,38 29,29 29,11" fill="#1e9ad6"/>
      <polygon points="133,2 150,11 150,29 133,38 116,29 116,11" fill="#7a7a7a"/>
      <polygon points="217,2 234,11 234,29 217,38 200,29 200,11" fill="#5f5f5f"/>
    </g>
    <g fill="none" stroke="#fff" stroke-width="1.4">
      <rect x="40" y="14" width="12" height="12" rx="1"/><rect x="127" y="14" width="12" height="12" rx="1"/><path d="M211 20 h12 M217 14 v12"/>
    </g>
  </svg>
  <div class="abs" style="left:42px;top:372px;width:264px;display:flex;justify-content:space-between">
    <div class="copy" style="position:static;width:76px"><p>Add a short note here that explains this idea in a few clear words for the reader.</p></div>
    <div class="copy" style="position:static;width:76px"><p>Add a short note here that explains this idea in a few clear words for the reader.</p></div>
    <div class="copy" style="position:static;width:76px"><p>Add a short note here that explains this idea in a few clear words for the reader.</p></div>
  </div>
  <footer class="footer"><span>Halden Consulting | © All Rights Reserved</span><span>Page | 11</span></footer>
</section>

<section class="page inner c3 r4">
  <div class="header-brand"><div class="brand brand-sm"><span class="dot"></span>HALDEN</div></div>
  <h2 class="heading" style="top:60px">Table &amp; Chart 1</h2>
  <table class="grid" style="top:90px">
    <tr><th class="b">TEXT HERE</th><th class="g">TEXT</th><th class="d">TEXT</th></tr>
    <tr><td>Add Contents Title</td><td>Add Contents Title</td><td>Add Contents Title</td></tr>
    <tr><td>Modern word template</td><td>Modern word template</td><td>Modern word template</td></tr>
    <tr><td>Add Contents Title</td><td>Add Contents Title</td><td>Add Contents Title</td></tr>
    <tr><td>Modern word template</td><td>Modern word template</td><td>Modern word template</td></tr>
    <tr><td>Add Contents Title</td><td>Add Contents Title</td><td>Add Contents Title</td></tr>
    <tr><td>Modern word template</td><td>Modern word template</td><td>Modern word template</td></tr>
    <tr><td>Add Contents Title</td><td>Add Contents Title</td><td>Add Contents Title</td></tr>
    <tr><td>Modern word template</td><td>Modern word template</td><td>Modern word template</td></tr>
    <tr><td>Add Contents Title</td><td>Add Contents Title</td><td>Add Contents Title</td></tr>
  </table>
  <div class="copy" style="top:247px"><p>Use this space to outline the key ideas of the session, the goals set for each participant and the practical tools they will take back to their team. Keep every point short, clear and easy to revisit after the workshop ends, so leaders can return to these notes when a real decision is on the table and apply what they learned with confidence.</p></div>
  <div class="abs" style="left:0;width:100%;top:316px;text-align:center;font-size:6px;color:var(--ink)">Chart Title</div>
  <svg class="abs" style="left:42px;top:330px" width="266" height="110" viewBox="0 0 266 110" aria-hidden="true">
    <g stroke="#eee" stroke-width="0.6"><path d="M14 8H262M14 23H262M14 38H262M14 53H262M14 68H262M14 83H262"/></g>
    <g font-family="Open Sans, sans-serif" font-size="3.6" fill="#777" text-anchor="end">
      <text x="10" y="10">6</text><text x="10" y="25">5</text><text x="10" y="40">4</text><text x="10" y="55">3</text><text x="10" y="70">2</text><text x="10" y="85">1</text><text x="10" y="100">0</text>
    </g>
    <g>
      <rect x="30" y="33" width="8" height="65" fill="#1e9ad6"/><rect x="40" y="62" width="8" height="36" fill="#a8a8a8"/><rect x="50" y="68" width="8" height="30" fill="#6b6b6b"/>
      <rect x="90" y="60" width="8" height="38" fill="#1e9ad6"/><rect x="100" y="32" width="8" height="66" fill="#a8a8a8"/><rect x="110" y="68" width="8" height="30" fill="#6b6b6b"/>
      <rect x="150" y="45" width="8" height="53" fill="#1e9ad6"/><rect x="160" y="71" width="8" height="27" fill="#a8a8a8"/><rect x="170" y="53" width="8" height="45" fill="#6b6b6b"/>
      <rect x="210" y="30" width="8" height="68" fill="#1e9ad6"/><rect x="220" y="56" width="8" height="42" fill="#a8a8a8"/><rect x="230" y="23" width="8" height="75" fill="#6b6b6b"/>
    </g>
    <path d="M14 98H262" stroke="#ccc" stroke-width="0.6"/>
    <g font-family="Open Sans, sans-serif" font-size="3.6" fill="#777" text-anchor="middle">
      <text x="44" y="104">Category 1</text><text x="104" y="104">Category 2</text><text x="164" y="104">Category 3</text><text x="224" y="104">Category 4</text>
    </g>
    <g font-family="Open Sans, sans-serif" font-size="3.4" fill="#777">
      <rect x="100" y="106" width="3" height="3" fill="#1e9ad6"/><text x="105" y="109">Series 1</text>
      <rect x="122" y="106" width="3" height="3" fill="#a8a8a8"/><text x="127" y="109">Series 2</text>
      <rect x="144" y="106" width="3" height="3" fill="#6b6b6b"/><text x="149" y="109">Series 3</text>
    </g>
  </svg>
  <footer class="footer"><span>Halden Consulting | © All Rights Reserved</span><span>Page | 12</span></footer>
</section>

<!-- Row 5 -->
<section class="page inner c1 r5">
  <div class="header-brand"><div class="brand brand-sm"><span class="dot"></span>HALDEN</div></div>
  <h2 class="heading" style="top:61px">Text with table</h2>
  <div class="band" style="top:83px;height:65px"></div>
  <div class="abs" style="left:40px;top:90px;font-size:38px;font-weight:700;color:#fff;line-height:50px">01</div>
  <div class="copy" style="left:120px;top:96px;width:186px;color:#fff"><p>Add a short introduction to this section here. Say what the reader will learn, why it matters for their role and how the table below supports the key message.</p></div>
  <div class="abs" style="left:42px;top:164px;font-size:6px;color:var(--ink)">Content Tile 01</div>
  <div class="copy" style="top:185px"><p>Use this space to outline the key ideas of the session, the goals set for each participant and the practical tools they will take back to their team. Keep every point short, clear and easy to revisit after the workshop ends, so leaders can return to these notes when a real decision is on the table and apply what they learned with confidence.</p></div>
  <div class="abs" style="left:42px;top:262px;font-size:6px;color:var(--ink)">Content Tile 02</div>
  <div class="copy" style="top:283px"><p>Each module opens with a short overview of the theme, followed by guided questions, worked examples and a space for personal reflection and action planning. Write the purpose of the programme here, who it is designed for and how the material should be used during and after each session, with links between slides and workbook.</p></div>
  <table class="grid" style="top:362px">
    <tr><th class="b">Content 1</th><th class="g">Content 2</th><th class="d">Content 3</th></tr>
    <tr><td>Modern word template</td><td>Modern word template</td><td>Modern word template</td></tr>
    <tr><td>Add Contents Title</td><td>Add Contents Title</td><td>Add Contents Title</td></tr>
    <tr><td>Modern word template</td><td>Modern word template</td><td>Modern word template</td></tr>
    <tr><td>Add Contents Title</td><td>Add Contents Title</td><td>Add Contents Title</td></tr>
    <tr><td>Modern word template</td><td>Modern word template</td><td>Modern word template</td></tr>
  </table>
  <footer class="footer"><span>Halden Consulting | © All Rights Reserved</span><span>Page | 13</span></footer>
</section>

<section class="page inner c2 r5">
  <div class="header-brand"><div class="brand brand-sm"><span class="dot"></span>HALDEN</div></div>
  <h2 class="heading" style="top:60px">Infographic 1</h2>
  <svg class="abs" style="left:41px;top:99px" width="110" height="110" viewBox="0 0 110 110" aria-hidden="true">
    <g stroke="#fff" stroke-width="2">
      <polygon points="55,3 100,29 72.3,45 55,35" fill="#1e9ad6"/>
      <polygon points="100,29 100,81 72.3,65 72.3,45" fill="#7a7a7a"/>
      <polygon points="100,81 55,107 55,75 72.3,65" fill="#1e9ad6"/>
      <polygon points="55,107 10,81 37.7,65 55,75" fill="#7a7a7a"/>
      <polygon points="10,81 10,29 37.7,45 37.7,65" fill="#1e9ad6"/>
      <polygon points="10,29 55,3 55,35 37.7,45" fill="#7a7a7a"/>
    </g>
    <g fill="none" stroke="#fff" stroke-width="1.2">
      <circle cx="71.5" cy="26.4" r="5"/><circle cx="88" cy="55" r="5"/><circle cx="71.5" cy="83.6" r="5"/><circle cx="38.5" cy="83.6" r="5"/><circle cx="22" cy="55" r="5"/><circle cx="38.5" cy="26.4" r="5"/>
    </g>
  </svg>
  <div class="abs" style="left:168px;top:116px;font-size:6px;color:var(--ink)">Content 01</div>
  <div class="copy" style="left:168px;top:128px;width:138px"><p>Add a short note here on how these six parts fit together as one model. Keep each point clear and easy to revisit, and link it to a real example the group can discuss in pairs.</p></div>
  <h2 class="heading" style="top:234px">Infographic 2</h2>
  <svg class="abs" style="left:0;top:270px" width="348" height="140" viewBox="0 270 348 140" aria-hidden="true">
    <g fill="none" stroke-width="8">
      <circle cx="78" cy="360" r="35" stroke="#1e9ad6" stroke-dasharray="165 55" transform="rotate(-40 78 360)"/>
      <circle cx="121" cy="311" r="35" stroke="#8a8a8a" stroke-dasharray="165 55" transform="rotate(140 121 311)"/>
      <circle cx="170" cy="360" r="35" stroke="#6b6b6b" stroke-dasharray="165 55" transform="rotate(-40 170 360)"/>
      <circle cx="220" cy="311" r="35" stroke="#1e9ad6" stroke-dasharray="165 55" transform="rotate(140 220 311)"/>
      <circle cx="265" cy="360" r="35" stroke="#8a8a8a" stroke-dasharray="165 55" transform="rotate(-40 265 360)"/>
    </g>
    <g>
      <circle cx="78" cy="360" r="20" fill="#1e9ad6"/><circle cx="121" cy="311" r="20" fill="#8a8a8a"/><circle cx="170" cy="360" r="20" fill="#6b6b6b"/><circle cx="220" cy="311" r="20" fill="#1e9ad6"/><circle cx="265" cy="360" r="20" fill="#8a8a8a"/>
    </g>
    <g fill="none" stroke="#fff" stroke-width="1.6" stroke-linecap="round">
      <circle cx="78" cy="357" r="5"/><path d="M76 364h4"/>
      <circle cx="121" cy="311" r="7"/><path d="M121 306v5h4"/>
      <path d="M162 366v-5M168 366v-9M174 366v-7M180 366v-12"/>
      <circle cx="214" cy="308" r="2.5"/><circle cx="226" cy="308" r="2.5"/><path d="M209 318q5-6 10 0M221 318q5-6 10 0"/>
      <path d="M257 362l6-5 5 4 6-6"/>
    </g>
  </svg>
  <footer class="footer"><span>Halden Consulting | © All Rights Reserved</span><span>Page | 14</span></footer>
</section>

<section class="page c3 r5 dark">
  <div class="rule" style="left:42px;top:43px;background:#fff"></div>
  <h2 class="abs" style="left:42px;top:52px;font-size:17px;font-weight:600;color:#fff">Section Title Here</h2>
  <div class="copy" style="top:86px;color:#fff"><p>Add a short line here that introduces the theme of this section and what the reader should focus on.</p></div>
  <div class="abs" style="left:42px;top:392px;font-size:56px;font-weight:700;color:#fff;line-height:70px">02</div>
</section>

<!-- Row 6 -->
<section class="page inner c1 r6">
  <div class="header-brand"><div class="brand brand-sm"><span class="dot"></span>HALDEN</div></div>
  <h2 class="heading" style="top:61px">Profile Data Section</h2>

  <div class="photo" role="img" aria-label="Portrait photo of team member one" style="left:42px;top:106px;width:64px;height:68px;background:linear-gradient(160deg,#cfcfcf,#6d6d6d)"></div>
  <div class="abs" style="left:114px;top:104px;font-size:6px;color:var(--blue)">Profile Name 01</div>
  <div class="copy" style="left:114px;top:116px;width:192px"><p>Add a short profile here with the role, key skills and the areas this person covers within the programme.</p></div>
  <div class="socials" style="left:114px;top:160px;color:#666"><span></span><span></span><span></span><span></span></div>

  <div class="photo" role="img" aria-label="Portrait photo of team member two" style="left:42px;top:185px;width:64px;height:68px;background:linear-gradient(160deg,#d8d8d8,#5e5e5e)"></div>
  <div class="abs" style="left:114px;top:183px;font-size:6px;color:var(--blue)">Profile Name 02</div>
  <div class="copy" style="left:114px;top:195px;width:192px"><p>Add a short profile here with the role, key skills and the areas this person covers within the programme.</p></div>
  <div class="socials" style="left:114px;top:239px;color:#666"><span></span><span></span><span></span><span></span></div>

  <div class="photo" role="img" aria-label="Portrait photo of team member three" style="left:42px;top:263px;width:64px;height:68px;background:linear-gradient(160deg,#e6e6e6,#777)"></div>
  <div class="abs" style="left:114px;top:261px;font-size:6px;color:var(--blue)">Profile Name 03</div>
  <div class="copy" style="left:114px;top:273px;width:192px"><p>Add a short profile here with the role, key skills and the areas this person covers within the programme.</p></div>
  <div class="socials" style="left:114px;top:317px;color:#666"><span></span><span></span><span></span><span></span></div>

  <div class="photo" role="img" aria-label="Portrait photo of team member four" style="left:42px;top:341px;width:64px;height:68px;background:linear-gradient(160deg,#bdbdbd,#3f3f3f)"></div>
  <div class="abs" style="left:114px;top:339px;font-size:6px;color:var(--blue)">Profile Name 04</div>
  <div class="copy" style="left:114px;top:351px;width:192px"><p>Add a short profile here with the role, key skills and the areas this person covers within the programme.</p></div>
  <div class="socials" style="left:114px;top:395px;color:#666"><span></span><span></span><span></span><span></span></div>

  <footer class="footer"><span>Halden Consulting | © All Rights Reserved</span><span>Page | 16</span></footer>
</section>

<section class="page inner c2 r6">
  <div class="header-brand"><div class="brand brand-sm"><span class="dot"></span>HALDEN</div></div>
  <h2 class="heading" style="top:61px">Additional Notes</h2>
  <div class="abs" style="left:42px;top:90px;font-size:5.5px;color:var(--ink)">Hello</div>
  <div class="copy" style="top:102px"><p>Use this page for any closing notes, follow up tasks or contacts the group may need once the course ends. Add a short thank you and a reminder of the next session date, along with where the slides and the workbook can be found.</p></div>
  <div class="abs" style="left:42px;top:160px;font-size:5.5px;font-style:italic;color:var(--ink)">- Name Here</div>
  <footer class="footer"><span>Halden Consulting | © All Rights Reserved</span><span>Page | 17</span></footer>
</section>

<section class="page c3 r6">
  <div class="rule" style="left:29px;top:39px"></div>
  <h2 class="abs" style="left:29px;top:48px;font-size:20px;font-weight:700;color:var(--grey-dark)">Thank You</h2>
  <div class="abs" style="left:42px;top:284px"><div class="brand brand-lg"><span class="dot"></span>HALDEN</div></div>
  <div class="abs" style="left:45px;top:335px;font-size:9px;font-weight:600;color:var(--ink)">Add Name Here</div>
  <svg class="abs" style="left:38px;top:368px" width="16" height="90" viewBox="0 0 16 90" aria-hidden="true">
    <path d="M3 2c2 0 3 3 3 4s-2 1-1 3 3 4 5 5 2-1 3-1 4 1 4 3-2 3-4 3C7 19-1 10 0 5c0-2 1-3 3-3z" fill="#1e9ad6"/>
    <circle cx="8" cy="32" r="6" fill="none" stroke="#1e9ad6" stroke-width="1.4"/><path d="M2 32h12M8 26c-3 4-3 8 0 12M8 26c3 4 3 8 0 12" fill="none" stroke="#1e9ad6" stroke-width="1"/>
    <rect x="1" y="51" width="14" height="10" fill="#1e9ad6"/><path d="M1 51l7 6 7-6" fill="none" stroke="#fff" stroke-width="1"/>
    <path d="M8 88c-4-5-6-8-6-11a6 6 0 0 1 12 0c0 3-2 6-6 11z" fill="#1e9ad6"/><circle cx="8" cy="77" r="2" fill="#fff"/>
  </svg>
  <div class="abs" style="left:67px;top:374px;font-size:6.5px;color:var(--ink);line-height:24.3px">
    +1 234 567 890<br>www.yourwebsite.com<br>addyouremail@here.com<br>Add your location here
  </div>
</section>

</body>
</html>
```